Halt and Thicken New Branding Stationary Set - updated Oct 30th 2017

Updated on 30th Oct 2017 as we now need a whole folder design instead of a folder cover. We have thought out exactly what should be on it so it wont be hard. We are happy for this to be completed only by the winning designer if you like. And also we are guaranteeing this project now. Thanks!

We just got our new logo and now we would like a stationary set so we can brand our company communications. The items we need designed are:
Business cards
Letterhead
Appointment confirmation cards
Folder - switched from folder cover. Note that if you don't wish to do this unless you are selected as the winner this is fine.

1. Business cards - for 5 employees, final names will be given once the winner is selected, but you can use this one as the sample:
Lucinda Marquez
Hair Regrowth Expert
Halt and Thicken
7182 Oakmere Ave, Suite 500
Beverly Hills CA 90299
lucinda@jamesholloway-md.example
(310) 555-0193

2. Letterhead 8.5" x 11.0" vertical
Halt and Thicken
Beverly Hills CA 90299
office@haltandthicken.example
(310) 555-0193

3. Appointment Confirmation cards - business card size
Halt and Thicken
Beverly Hills CA 90299
Appointment For:
Date:
Time:
If you are unable to make your appointment, please contact us to reschedule at:
(310) 555-0193
info@jamesholloway-md.example

*UPDATED*
4. Folder 9" x 12 " vertical with double pocket
We would like the infinity image from the logo made really big so the left side is on the back and the right side with the + sign is on the front and its takes up the maximum room on the folder.
On the front below the half logo it should say "A Biochemical Revolution..."
On the inside we would also like to have the infinity sign from the logo but faded and half on the left pocket half on the right.
On left inside pocket it should say (this will be partically written on top of the logo):
James Holloway MD
Precision Medicine
Halt and Thicken Hair
On the Right inside pocket it should say the following:
Because the Enemy of BETTER Health is Good Health
BETTER Ingredients
BETTER Recipe
BETTER Medicine
On the back below the logo on the bottom should be the contact information.
I attached a picture of our drawing of what we want for this to make it easier.

Here is our website to give you an idea of our branding: http://www.haltandthicken.example/

We are the only true cure for hair loss and need to look professional and highest quality and beyond reproach from an ethical standpoint. We are a medical clinic so this should be portrayed also.
We cured hair loss by analyzing biochemistry and rebalancing it so that the process reverses and your own hair can grow back naturally.

Business card information:

OK so here is the information for the business cards:

Lucinda Marquez
Hair Regrowth Expert
(310) 555-0193
www.haltandthicken.example

Marisol Quintero
Hair Growth Consultant
(310) 555-0193
marisol@jamesholloway-md.example
www.haltandthicken.example

Janice Pelham
CMO/COO
(310) 555-0193
janice@haltandthicken.example
www.haltandthicken.example

Dr Glen Holloway
President
(310) 555-0193
info@jamesholloway-md.example
www.haltandthicken.example

Halt and Thicken
Customer Service
(310) 555-0193
info@jamesholloway-md.example
www.haltandthicken.example

Target Market(s)

Men aged 20-24 who care about their appearance, care about their hair and care about the world.

Industry/Entity Type

Medical And Science

Font styles to use
Sans Serif

Colors
00a990
ffffff
9d9d9d
333333

Requirements
Must have
• Must use the logo and our brand colors from the logo in all designs.
• The pantone colors are:
• Green: #4ca26f
• Light Grey: #999999
• The design should be symmetrical and balanced.
Nice to have
• It should look reasonably masculine.
Should not have
• Do not include any red in the design.

```html
<!DOCTYPE html>
<html lang="en">
<head>
<meta charset="utf-8">
<title>Halt and Thicken — Presentation Folder, Inside Spread</title>
<link href="https://fonts.googleapis.com/css2?family=Arimo:wght@400;700&display=swap" rel="stylesheet">
<style>
  :root {
    --green: #009a6a;
    --green-dark: #008a5f;
    --grey: #9d9d9d;
    --ink: #333333;
    --paper: #ffffff;
    --paper-shade: #f4f4f4;
    --backdrop: #e6e6e6;
    --pale: #d9efe5;
  }
  * { box-sizing: border-box; margin: 0; padding: 0; }
  html, body {
    width: 1200px; height: 823px; overflow: hidden;
    background: var(--backdrop);
    font-family: "Arimo", Arial, sans-serif;
  }
  .canvas { position: relative; width: 1200px; height: 823px; }

  .panel {
    position: absolute; top: 41px; width: 555px; height: 740px;
    background: var(--paper);
    box-shadow: 0 6px 22px rgba(0,0,0,0.14);
  }
  .panel--left { left: 45px; background: linear-gradient(90deg, var(--paper-shade), var(--paper) 60%); }
  .panel--right { left: 600px; }
  .spine {
    position: absolute; left: 597px; top: 41px; width: 6px; height: 740px;
    background: linear-gradient(90deg, #cfcfcf, #e9e9e9, #cfcfcf);
  }

  .insert {
    position: absolute; left: 18px; top: 14px; right: 22px; height: 700px;
    background: var(--paper);
    box-shadow: 0 0 4px rgba(0,0,0,0.08);
  }

  .brand {
    position: absolute; left: 34px; top: 48px;
    display: flex; align-items: center; gap: 8px;
  }
  .brand__dot { width: 14px; height: 14px; border-radius: 50%; background: var(--green); }
  .brand__name { font-size: 13px; font-weight: 700; color: var(--green); letter-spacing: 0.3px; text-transform: uppercase; }

  .contact {
    position: absolute; right: 24px; top: 42px;
    border-left: 2px solid var(--green); padding-left: 7px;
    font-size: 7px; line-height: 10px; color: var(--ink);
  }
  .contact__group + .contact__group { margin-top: 5px; }
  .contact__line { display: flex; align-items: center; gap: 4px; }
  .contact__icon { width: 6px; height: 6px; fill: var(--green); }

  .pocket {
    position: absolute; top: 540px; width: 555px; height: 241px;
    background: var(--green); color: var(--paper);
  }
  .pocket--left { left: 45px; border-top-right-radius: 16px; }
  .pocket--right { left: 600px; border-top-left-radius: 16px; background: var(--green-dark); background: linear-gradient(180deg, var(--green), var(--green-dark)); }

  .signature { position: absolute; left: 92px; top: 110px; }
  .signature__name { font-size: 15px; font-weight: 700; }
  .signature__role { font-size: 13px; color: var(--pale); margin-top: 2px; }
  .signature__unit { font-size: 13px; margin-top: 14px; }

  .promise { position: absolute; left: 300px; top: 48px; width: 230px; }
  .promise__lead { font-size: 12.5px; line-height: 16px; }
  .promise__lead strong { font-weight: 700; }
  .promise__list { list-style: none; margin-top: 10px; }
  .promise__item { display: flex; align-items: center; gap: 8px; font-size: 13px; line-height: 26px; }
  .promise__tick { width: 12px; height: 12px; }
</style>
</head>
<body>
<main class="canvas">
  <section class="panel panel--left" aria-label="Inside left panel"></section>
  <section class="panel panel--right" aria-label="Inside right panel">
    <article class="insert" aria-label="Letterhead insert">
      <div class="brand">
        <span class="brand__dot"></span>
        <span class="brand__name">Halt and Thicken</span>
      </div>
      <address class="contact">
        <div class="contact__group">
          <div>7182 Oakmere Ave, Suite 500</div>
          <div>Beverly Hills CA 90299</div>
        </div>
        <div class="contact__group">
          <div class="contact__line"><svg class="contact__icon" viewBox="0 0 10 10"><path d="M2 0h2l1 3-1.5 1a6 6 0 0 0 2.5 2.5L7 5l3 1v2a2 2 0 0 1-2 2A8 8 0 0 1 0 2a2 2 0 0 1 2-2z"/></svg>(310) 555-0193</div>
          <div class="contact__line"><svg class="contact__icon" viewBox="0 0 10 10"><path d="M0 2h10v6H0zM0 2l5 3 5-3" stroke="#fff" stroke-width="0.8"/></svg>office@haltandthicken.example</div>
          <div class="contact__line"><svg class="contact__icon" viewBox="0 0 10 10"><circle cx="5" cy="5" r="5"/></svg>www.haltandthicken.example</div>
        </div>
      </address>
    </article>
  </section>
  <div class="spine"></div>

  <section class="pocket pocket--left" aria-label="Left pocket">
    <div class="signature">
      <div class="signature__name">James Holloway MD</div>
      <div class="signature__role">Precision Medicine</div>
      <div class="signature__unit">Halt and Thicken Hair</div>
    </div>
  </section>

  <section class="pocket pocket--right" aria-label="Right pocket">
    <div class="promise">
      <p class="promise__lead">Because the Enemy of BETTER Health<br><strong>is Good Health</strong></p>
      <ul class="promise__list">
        <li class="promise__item"><svg class="promise__tick" viewBox="0 0 12 12"><polyline points="1,6 4.5,10 11,1" fill="none" stroke="#ffffff" stroke-width="1.6"/></svg>BETTER Ingredients</li>
        <li class="promise__item"><svg class="promise__tick" viewBox="0 0 12 12"><polyline points="1,6 4.5,10 11,1" fill="none" stroke="#ffffff" stroke-width="1.6"/></svg>BETTER Recipe</li>
        <li class="promise__item"><svg class="promise__tick" viewBox="0 0 12 12"><polyline points="1,6 4.5,10 11,1" fill="none" stroke="#ffffff" stroke-width="1.6"/></svg>BETTER Medicine</li>
      </ul>
    </div>
  </section>
</main>
</body>
</html>
```